QM Interiors needs and Interior Design Business card

I can do anything from Commercial to Residential and Free lance. Beginning to end in design selection process.
Need something to catch the eye of potential customers and vendors. From furniture to Tile and Cabinet selections. I can do it all.

Industry/Entity Type

Design Agency

Contact Information for Business Card

QM Interiors- Design Consultanting Residential, Commerical
Maybe a cool detail background. Wall paper print that can have some texture

Font styles to use
Serif

Colors
709dcb
34a6d7
b868aa
e667a6
f59296
85acd3
ffffff
000000
5c5c5c

Requirements
Must have
• Square or Rectangular with Rounded edges
• Name
• Address
• Phone
• Email
Nice to have
• Some colored edges More simples not too busy
• Pattern detail in background.
Should not have
• Not too much color

```html
<!DOCTYPE html>
<html lang="en">
<head>
<meta charset="utf-8">
<title>QM Interiors – Business Card</title>
<link href="https://fonts.googleapis.com/css2?family=Lora:ital,wght@0,400;0,700;1,400&display=swap" rel="stylesheet">
<style>
  :root {
    --backdrop: #8a8a8a;
    --card-white: #ffffff;
    --brand-blue: #709dcb;
    --brand-sky: #34a6d7;
    --brand-plum: #b868aa;
    --ink-grey: #5c5c5c;
    --rule-grey: #85acd3;
    --white: #ffffff;
  }
  * { margin: 0; padding: 0; box-sizing: border-box; }
  html, body {
    width: 1105px;
    height: 1200px;
    overflow: hidden;
    background: var(--backdrop);
  }
  .canvas {
    position: relative;
    width: 1105px;
    height: 1200px;
  }
  .card {
    position: absolute;
    left: 182px;
    width: 746px;
    height: 426px;
    overflow: hidden;
    border-radius: 18px;
    font-family: "Lora", serif;
  }
  .card--front {
    top: 119px;
    background-color: var(--card-white);
    background-image: repeating-linear-gradient(45deg, rgba(112,157,203,0.06) 0 2px, transparent 2px 14px),
                      repeating-linear-gradient(-45deg, rgba(184,104,170,0.05) 0 2px, transparent 2px 14px);
    border-left: 10px solid var(--brand-blue);
  }
  .card--back {
    top: 635px;
    background-color: var(--brand-blue);
    background-image: repeating-linear-gradient(45deg, rgba(255,255,255,0.06) 0 2px, transparent 2px 14px),
                      repeating-linear-gradient(-45deg, rgba(255,255,255,0.05) 0 2px, transparent 2px 14px);
  }

  /* Front */
  .brand-dot {
    position: absolute;
    left: 113px;
    top: 43px;
    width: 110px;
    height: 110px;
    border: 6px solid var(--brand-blue);
    border-radius: 50%;
  }
  .brand-name {
    position: absolute;
    letter-spacing: 0.12em;
    white-space: nowrap;
    font-weight: 400;
  }
  .brand-name--front {
    left: 38px;
    top: 160px;
    font-size: 32px;
    color: var(--brand-plum);
  }
  .holder {
    position: absolute;
    left: 38px;
    top: 300px;
    white-space: nowrap;
  }
  .holder__name {
    font-size: 25px;
    font-weight: 700;
    color: var(--brand-sky);
  }
  .holder__role {
    font-size: 21px;
    color: var(--ink-grey);
  }
  .holder-rule {
    position: absolute;
    left: 38px;
    top: 342px;
    width: 650px;
    height: 2px;
    background: var(--rule-grey);
  }
  .contact-row {
    position: absolute;
    left: 38px;
    display: flex;
    gap: 18px;
    font-size: 19px;
    color: var(--ink-grey);
    white-space: nowrap;
  }
  .contact-row--main { top: 352px; }
  .contact-row--address { top: 384px; }
  .contact-item { display: flex; align-items: center; gap: 7px; }
  .contact-item svg { width: 17px; height: 17px; fill: var(--brand-sky); }

  /* Back */
  .back-ring {
    position: absolute;
    left: 0; top: 0;
    width: 746px; height: 426px;
  }
  .service-list {
    position: absolute;
    left: 48px;
    top: 218px;
    list-style: none;
    font-style: italic;
    font-size: 21px;
    line-height: 34.5px;
    color: var(--white);
  }
  .service-list li::before {
    content: "";
    display: inline-block;
    width: 8px; height: 8px;
    margin-right: 14px;
    border-radius: 50%;
    background: var(--white);
    vertical-align: middle;
  }
  .brand-name--back {
    left: 42px;
    top: 348px;
    font-size: 36px;
    color: var(--white);
  }
</style>
</head>
<body>
<main class="canvas">
  <section class="card card--front" aria-label="Business card front">
    <div class="brand-dot" aria-hidden="true"></div>
    <div class="brand-name brand-name--front">QM Interiors</div>
    <div class="holder">
      <span class="holder__name">Nora Pellisier -</span>
      <span class="holder__role">Design Consultant</span>
    </div>
    <div class="holder-rule"></div>
    <div class="contact-row contact-row--main">
      <span class="contact-item">
        <svg viewBox="0 0 24 24" aria-hidden="true"><path d="M6.6 10.8a15.1 15.1 0 0 0 6.6 6.6l2.2-2.2a1 1 0 0 1 1-.25 11.4 11.4 0 0 0 3.6.57 1 1 0 0 1 1 1V20a1 1 0 0 1-1 1A17 17 0 0 1 3 4a1 1 0 0 1 1-1h3.5a1 1 0 0 1 1 1c0 1.25.2 2.45.57 3.57a1 1 0 0 1-.25 1z"/></svg>
        555 014 2290
      </span>
      <span class="contact-item">
        <svg viewBox="0 0 24 24" aria-hidden="true"><path d="M2 5h20v2l-10 7L2 7z"/><path d="M2 9l10 7 10-7v10H2z"/></svg>
        studio@qmdemo.com
      </span>
      <span class="contact-item">
        <svg viewBox="0 0 24 24" aria-hidden="true"><circle cx="12" cy="12" r="10"/><path d="M7 8c2 0 3 1 3 3s2 2 2 4-1 3-1 4M15 5c0 2 1 3 3 3" fill="none" stroke="#ffffff" stroke-width="1.8"/></svg>
        qmdemo.com
      </span>
    </div>
    <div class="contact-row contact-row--address">
      <span class="contact-item">
        <svg viewBox="0 0 24 24" aria-hidden="true"><path d="M12 2a7 7 0 0 0-7 7c0 5 7 13 7 13s7-8 7-13a7 7 0 0 0-7-7zm0 9.5A2.5 2.5 0 1 1 12 6.5a2.5 2.5 0 0 1 0 5z"/></svg>
        214 Alder Row, Suite 3, Fairview, OR 97000
      </span>
    </div>
  </section>

  <section class="card card--back" aria-label="Business card back">
    <svg class="back-ring" viewBox="0 0 746 426" aria-hidden="true">
      <circle cx="582" cy="213" r="242" fill="none" stroke="#ffffff" stroke-width="9"/>
    </svg>
    <ul class="service-list">
      <li>Design Consulting</li>
      <li>Commercial</li>
      <li>Residential</li>
    </ul>
    <div class="brand-name brand-name--back">QM Interiors</div>
  </section>
</main>
</body>
</html>
```